Exciting Automotive Postcard/mailer

Our automotive transmission shop is expanding to include general repair and custom hot rod work. I would love a flashy postcard to mail to my previous customers to let them know that we can now take care of ALL of their repairs/maintenance... Something that reminds them that we are trustworthy and reliable---- and would love the opportunity to service all of their cars! Somewhere on the card I would like it to say "call Toby & Marcia to take care of all of your needs" We would like something flashy, colorful, incorporating our logo, our pooch, and automotive stuff..
Industry/Entity Type
Automotive
Look and feel
Each slider illustrates characteristics of the customer's brand and the style your logo design should communicate.

```html
<!DOCTYPE html>
<html lang="en">
<head>
<meta charset="utf-8">
<title>Ridgeway Auto Postcard</title>
<link rel="stylesheet" href="https://fonts.googleapis.com/css2?family=Open+Sans:ital,wght@0,400;0,600;0,700;0,800;1,700&display=swap">
<style>
  :root {
    --page: #e9e7e4;
    --card-dark: #2b2b2e;
    --card-mid: #3a3a3e;
    --card-light: #4a4a4f;
    --white: #ffffff;
    --red: #d9262b;
    --blue: #1c6fc2;
    --blue-dark: #124f8f;
    --yellow: #f3c316;
    --line-blue: #4a86c8;
    --text-soft: #e6e6e6;
    --stamp: #9aa7b5;
  }
  * { margin: 0; padding: 0; box-sizing: border-box; }
  html, body {
    width: 900px; height: 1200px; overflow: hidden;
    background: var(--page);
    font-family: "Open Sans", Arial, sans-serif;
  }
  .canvas { position: relative; width: 900px; height: 1200px; }

  .postcard {
    position: absolute; left: 60px; width: 780px; height: 510px;
    overflow: hidden; border-radius: 4px;
    box-shadow: 0 6px 18px rgba(0,0,0,.25);
  }
  .postcard--front { top: 50px; background: var(--card-dark); }
  .postcard--back { top: 640px; background: var(--white); }
  .backdrop { position: absolute; inset: 0; width: 100%; height: 100%; }

  /* front */
  .brand {
    position: absolute; left: 70px; top: 40px;
    display: flex; align-items: center; gap: 12px;
  }
  .brand__dot { width: 34px; height: 34px; border-radius: 50%; background: var(--red); }
  .brand__name { color: var(--white); font-weight: 700; font-size: 30px; letter-spacing: .5px; }

  .headline {
    position: absolute; left: 70px; top: 118px;
    color: var(--white); font-weight: 700; font-size: 58px; line-height: 1;
  }
  .headline__call {
    position: absolute; left: 455px; top: 92px;
    color: var(--red); font-weight: 700; font-size: 22px;
  }
  .tagline {
    position: absolute; left: 72px; top: 186px;
    color: var(--white); font-size: 26px; font-weight: 400;
  }

  .photo {
    position: absolute; border: 3px solid #5a5a60;
  }
  .photo--detail {
    left: 632px; top: 78px; width: 132px; height: 96px;
    background: linear-gradient(135deg, #8a8f96 0%, #5b6068 55%, #3e4248 100%);
  }
  .photo--shop {
    left: 262px; top: 186px; width: 502px; height: 158px;
    top: 232px;
    background: linear-gradient(180deg, #b9bcc0 0%, #8d8f93 35%, #6f5d52 70%, #4b4440 100%);
  }

  /* back */
  .back-panel { position: absolute; left: 0; top: 0; width: 380px; height: 100%; }
  .ribbon {
    position: absolute; left: 0; height: 34px; padding: 0 26px 0 22px;
    display: flex; align-items: center;
    color: var(--white); font-style: italic; font-weight: 700; font-size: 21px;
    background: linear-gradient(90deg, var(--blue-dark), var(--blue));
    clip-path: polygon(0 0, 100% 0, 90% 100%, 0 100%);
  }
  .ribbon--about { top: 150px; }
  .ribbon--contact { top: 295px; }
  .about-text {
    position: absolute; left: 22px; top: 200px; width: 290px;
    color: var(--text-soft); font-size: 17px; line-height: 1.4;
  }
  .about-text__lead { color: var(--yellow); font-weight: 800; font-size: 26px; }
  .contact-list { position: absolute; left: 24px; top: 345px; list-style: none; }
  .contact-list__item {
    display: flex; align-items: center; gap: 12px;
    color: var(--text-soft); font-size: 18px; margin-bottom: 14px;
  }
  .contact-list__icon { width: 20px; height: 20px; flex: none; }

  .stamp-box {
    position: absolute; right: 34px; top: 34px; width: 100px; height: 110px;
    border: 2px solid var(--stamp);
  }
  .address-line {
    position: absolute; left: 455px; width: 290px; height: 2px; background: var(--line-blue);
  }
  .address-line--1 { top: 290px; }
  .address-line--2 { top: 345px; }
  .address-line--3 { top: 400px; }
</style>
</head>
<body>
<main class="canvas">

  <section class="postcard postcard--front" aria-label="Postcard front">
    <svg class="backdrop" viewBox="0 0 780 510" preserveAspectRatio="none" aria-hidden="true">
      <polygon points="0,0 780,0 780,70 0,250" fill="#323236"/>
      <polygon points="0,360 780,220 780,510 0,510" fill="#3c3c41"/>
      <polygon points="0,430 780,330 780,510 0,510" fill="#2a2a2d"/>
      <polygon points="420,510 780,380 780,510" fill="#46464b"/>
    </svg>

    <div class="brand">
      <span class="brand__dot"></span>
      <span class="brand__name">Ridgeway Auto</span>
    </div>

    <span class="headline__call">Call</span>
    <h1 class="headline">Toby &amp; Marcia</h1>
    <p class="tagline">to take care of all of your needs</p>

    <div class="photo photo--detail" role="img" aria-label="Photo of a mechanic working under a car"></div>
    <div class="photo photo--shop" role="img" aria-label="Photo of the repair shop floor with cars on red lifts"></div>
  </section>

  <section class="postcard postcard--back" aria-label="Postcard back">
    <svg class="back-panel" viewBox="0 0 380 510" preserveAspectRatio="none" aria-hidden="true">
      <polygon points="0,0 340,0 380,510 0,510" fill="#2b2b2e"/>
      <polygon points="0,0 340,0 345,70 0,200" fill="#323236"/>
      <polygon points="0,380 370,270 380,510 0,510" fill="#3a3a3f"/>
      <polygon points="0,460 378,400 380,510 0,510" fill="#28282b"/>
    </svg>

    <div class="ribbon ribbon--about">About Us:</div>
    <p class="about-text"><span class="about-text__lead">We</span> are trustworthy and reliable---- and would love the opportunity to service all of their cars!</p>

    <div class="ribbon ribbon--contact">Contact Us:</div>
    <ul class="contact-list">
      <li class="contact-list__item">
        <svg class="contact-list__icon" viewBox="0 0 20 20" aria-hidden="true">
          <rect width="20" height="20" rx="3" fill="#1c6fc2"/>
          <path d="M6 4.5l2 0 1 3-1.3 1a7 7 0 0 0 3.8 3.8l1-1.3 3 1 0 2a1.5 1.5 0 0 1-1.6 1.5A10 10 0 0 1 4.5 6.1 1.5 1.5 0 0 1 6 4.5z" fill="#fff"/>
        </svg>
        0123-555-019
      </li>
      <li class="contact-list__item">
        <svg class="contact-list__icon" viewBox="0 0 20 20" aria-hidden="true">
          <rect width="20" height="20" rx="3" fill="#1c6fc2"/>
          <rect x="4" y="6" width="12" height="8.5" fill="none" stroke="#fff" stroke-width="1.4"/>
          <path d="M4 6l6 5 6-5" fill="none" stroke="#fff" stroke-width="1.4"/>
        </svg>
        hello@ridgewayauto.com
      </li>
    </ul>

    <div class="stamp-box"></div>
    <div class="address-line address-line--1"></div>
    <div class="address-line address-line--2"></div>
    <div class="address-line address-line--3"></div>
  </section>

</main>
</body>
</html>
```